Redesign of PTO Calendar website

Looking to drastically improve our PTO (paid time off) Calendar look and feel. Need a modern and well thought out design that is fun.
Current Screenshots
https://files.brinvola.net/sheet/d/7vRt2mWq9LpZa4XkeN8sBy3dHcJ0fUoT6iQgEwMnY/view?mode=sharing
It's written in PHP and Laravel, if that matters. I am not necessarily attached to any of the current design, so please go wild. Current functionality needs to remain the same, but some can be added if you feel it would be of value. Layout can certainly change.
NOTE - this calendar can be used by any company, not just our own. So we'd like it to have a look and feel that is easy to navigate.
Site logo is attached.
Pages needed:
* Login Page
* Registration Page
* Calendar page
* Add PTO method
* Admin page (will use template for all admin areas)
* User profile page
Thanks!

```html
<!DOCTYPE html>
<html lang="en">
<head>
<meta charset="utf-8">
<title>Restday – PTO Calendar screens</title>
<link href="https://fonts.googleapis.com/css2?family=Montserrat:wght@500;600;700&family=Lato:wght@400;700&display=swap" rel="stylesheet">
<style>
:root{
  --page:#e1e1e1;
  --white:#ffffff;
  --sky:#29a8e0;
  --sky-dark:#0f7fcb;
  --navy-title:#1e7fc4;
  --slate:#3c4b59;
  --cell:#efefef;
  --cell-line:#e2e2e2;
  --text:#333a40;
  --muted:#8a8f94;
  --faint:#cfcfcf;
  --ev-cyan:#84e0ee;
  --ev-cyan-bar:#3fc6e0;
  --ev-green:#80e0c1;
  --ev-green-bar:#17b07a;
  --ev-blue:#8ccdee;
  --ev-blue-bar:#2fa6df;
  --save:#5fd6f6;
  --shade:rgba(4,18,24,.66);
}
*{box-sizing:border-box;margin:0;padding:0}
html,body{width:1200px;height:2965px;overflow:hidden;background:var(--page)}
body{font-family:'Lato',sans-serif;color:var(--text)}
.board{position:absolute;left:0;top:0;width:1043px;height:2577px;transform:scale(1.1505);transform-origin:0 0}

.screen{position:absolute;left:138px;width:767px;background:var(--white);box-shadow:0 2px 8px rgba(0,0,0,.08);overflow:hidden}
.screen--calendar{top:145px;height:784px}
.screen--modal{top:1015px;height:784px}
.screen--admin{top:1904px;height:527px}

/* sidebar */
.sidebar{position:absolute;left:0;top:0;width:121px;background:var(--sky);color:var(--white)}
.screen--calendar .sidebar,.screen--modal .sidebar{height:728px}
.screen--admin .sidebar{height:448px;background:var(--sky-dark)}
.brand{height:80px;display:flex;align-items:center;justify-content:center;gap:6px;font-family:'Montserrat',sans-serif;font-weight:700;font-size:17px;letter-spacing:.5px;border-bottom:1px solid rgba(255,255,255,.25)}
.brand-dot{width:10px;height:10px;border-radius:50%;background:var(--white)}
.nav-item{height:75px;display:flex;flex-direction:column;align-items:center;justify-content:center;gap:6px;font-family:'Montserrat',sans-serif;font-weight:700;font-size:12px;border-bottom:1px solid rgba(255,255,255,.25)}
.nav-item svg{width:28px;height:28px;stroke:var(--white);fill:none;stroke-width:1.4}
.nav-item.is-active{background:var(--sky-dark)}
.screen--admin .nav-item.is-active{background:var(--slate)}

/* top bar */
.topbar{position:absolute;left:121px;top:0;right:0;height:43px;background:var(--white);box-shadow:0 1px 3px rgba(0,0,0,.1)}
.user-chip{position:absolute;left:16px;top:11px;display:flex;align-items:center;gap:16px;font-size:11px;font-family:'Montserrat',sans-serif;font-weight:500;color:#555}
.avatar{width:21px;height:21px;border-radius:50%;background:linear-gradient(135deg,#9aa0a4,#4f565b);display:block}
.caret{font-size:8px;margin-left:-8px}
.tools{position:absolute;right:0;top:0;height:43px;display:flex;background:var(--slate)}
.screen--admin .tools{background:var(--sky)}
.tool{width:53px;display:flex;flex-direction:column;align-items:center;justify-content:center;gap:5px;color:var(--white);font-size:6px;font-weight:700;letter-spacing:.1px;border-left:1px solid rgba(255,255,255,.12)}
.tool svg{width:14px;height:14px;stroke:var(--white);fill:none;stroke-width:1.4}
.search{position:absolute;left:24px;top:7px;width:262px;height:29px;border:1px solid #e4e4e4;display:flex}
.search span{flex:1;font-size:10px;color:#777;padding:8px 0 0 12px}
.search b{width:27px;background:var(--sky-dark);display:flex;align-items:center;justify-content:center}
.search svg{width:11px;height:11px;stroke:var(--white);fill:none;stroke-width:2}

/* calendar */
.today-title{position:absolute;left:260px;top:70px;font-family:'Montserrat',sans-serif;font-weight:700;font-size:20px;color:var(--navy-title);letter-spacing:.3px}
.today-person{position:absolute;left:528px;top:72px;display:flex;gap:15px;align-items:center;font-family:'Montserrat',sans-serif;font-size:10px;line-height:12px;color:#555}
.today-person .avatar{width:22px;height:22px;position:relative}
.online{position:absolute;right:-1px;bottom:-1px;width:7px;height:7px;border-radius:50%;background:#2cc26c;border:1px solid var(--white)}
.toolbar{position:absolute;left:132px;top:135px;width:626px;height:28px}
.btn-plain{position:absolute;top:0;height:28px;border:1px solid #e2e2e2;background:var(--white);display:flex;align-items:center;justify-content:center;font-size:10px;font-family:'Montserrat',sans-serif;font-weight:600;color:#333}
.month-label{position:absolute;left:0;right:0;top:4px;text-align:center;font-family:'Montserrat',sans-serif;font-weight:700;font-size:18px;color:var(--navy-title)}
.view-switch{position:absolute;right:0;top:0;display:flex;border:1px solid #e2e2e2}
.view-switch span{width:52px;height:28px;display:flex;align-items:center;justify-content:center;font-size:10px;font-family:'Montserrat',sans-serif;font-weight:600;background:var(--white)}
.view-switch .is-on{background:var(--sky);color:var(--white)}
.calendar{position:absolute;left:132px;top:173px;width:626px}
.cal-head{display:grid;grid-template-columns:repeat(7,1fr);height:34px;background:var(--sky);margin:0 2px}
.cal-head span{display:flex;align-items:center;justify-content:center;color:var(--white);font-size:10px;font-family:'Montserrat',sans-serif;font-weight:600;border-right:1px solid rgba(255,255,255,.35)}
.cal-grid{display:grid;grid-template-columns:repeat(7,1fr);grid-auto-rows:87px;background:var(--cell);margin-top:2px}
.day{border-right:1px solid var(--cell-line);border-bottom:1px solid var(--cell-line);padding:6px 5px 0 9px;font-size:10px;line-height:14.5px;position:relative;overflow:hidden;min-width:0}
.day-num{display:block;text-align:right;font-weight:700;color:#555;font-size:10px}
.day.is-out .day-num{color:var(--faint);font-weight:400}
.day .ev{display:block;white-space:nowrap;letter-spacing:-.1px}
.ev-cyan,.ev-green,.ev-blue{padding-left:5px;padding-right:3px}
.ev-cyan{background:var(--ev-cyan);border-left:5px solid var(--ev-cyan-bar)}
.ev-green{background:var(--ev-green);border-left:5px solid var(--ev-green-bar)}
.ev-blue{background:var(--ev-blue);border-left:5px solid var(--ev-blue-bar)}
.ev-green .ev,.ev-blue .ev{margin-top:10px}
.footer{position:absolute;left:0;right:0;text-align:center;font-size:10px;color:#555}
.screen--calendar .footer,.screen--modal .footer{top:755px}
.screen--admin .footer{top:484px}

/* modal */
.shade{position:absolute;inset:0;background:var(--shade)}
.modal{position:absolute;left:188px;top:58px;width:392px;height:441px;background:var(--white)}
.modal-head{height:37px;background:var(--sky);color:var(--white);display:flex;align-items:center;justify-content:center;font-family:'Montserrat',sans-serif;font-weight:700;font-size:17px;position:relative}
.modal-close{position:absolute;right:12px;top:10px;font-size:15px}
.field-label{position:absolute;left:18px;font-size:10px;color:#555}
.field{position:absolute;left:18px;width:356px;height:32px;border:1px solid #e0e0e0;font-size:10px;color:#555;padding:10px 0 0 14px}
.field .arrow{position:absolute;right:12px;top:10px;font-size:7px}
.field svg{position:absolute;right:10px;top:10px;width:11px;height:11px;stroke:#666;fill:none;stroke-width:1.3}
.modal-btn{position:absolute;top:369px;width:80px;height:32px;color:var(--white);font-size:10px;font-weight:700;display:flex;align-items:center;justify-content:center}
.modal-btn--close{left:110px;background:var(--sky)}
.modal-btn--save{left:202px;background:var(--save)}

/* admin table */
.entries{position:absolute;left:306px;top:75px;display:flex;align-items:center;gap:24px;font-family:'Montserrat',sans-serif;font-size:10px;font-weight:600;color:var(--navy-title)}
.entries .select{width:46px;height:28px;border:1px solid #e0e0e0;display:flex;align-items:center;justify-content:center;gap:8px;color:#333}
.table-card{position:absolute;left:132px;top:113px;width:626px;height:335px;background:var(--cell)}
.data-table{width:622px;margin-left:2px;border-collapse:collapse;table-layout:fixed;font-size:10px}
.data-table th{background:var(--sky-dark);color:var(--white);height:33px;font-family:'Montserrat',sans-serif;font-weight:600;font-size:8.5px;white-space:nowrap;letter-spacing:-.1px;border-right:1px solid rgba(255,255,255,.35)}
.data-table td{height:63px;text-align:center;color:#555;border-right:1px solid var(--cell-line);border-bottom:1px solid var(--cell-line);line-height:16.5px;padding:0 4px}
.data-table .link{color:var(--navy-title);margin-left:22px}
.showing{position:absolute;left:0;right:0;top:253px;text-align:center;font-size:10px;color:#555}
.pager{position:absolute;left:248px;top:279px;width:128px;height:35px;background:var(--white);border:1px solid #e2e2e2;display:flex;align-items:center;font-size:10px;color:#333}
.pager span{padding:0 8px;border-right:1px solid #e4e4e4}
.pager span:last-child{border:none;padding-left:14px}
</style>
</head>
<body>
<div class="board">

  <!-- Calendar screen -->
  <section class="screen screen--calendar">
    <aside class="sidebar">
      <div class="brand">RESTDAY<span class="brand-dot"></span></div>
      <div class="nav-item"><svg viewBox="0 0 28 28"><circle cx="9" cy="9" r="4"/><circle cx="19" cy="9" r="4"/><circle cx="14" cy="18" r="4"/><path d="M6 26c1-3 4-4 8-4s7 1 8 4"/></svg>TEAMS</div>
      <div class="nav-item"><svg viewBox="0 0 28 28"><circle cx="14" cy="9" r="5"/><path d="M5 26c1-6 5-9 9-9s8 3 9 9"/><circle cx="20" cy="21" r="3"/></svg>MEMBERS</div>
      <div class="nav-item"><svg viewBox="0 0 28 28"><rect x="4" y="5" width="20" height="18"/><rect x="7" y="8" width="14" height="12"/><path d="M7 18l5-5 4 4 2-2 3 3"/></svg>PTO TYPES</div>
      <div class="nav-item is-active"><svg viewBox="0 0 28 28"><path d="M6 3h12l3 3v10M6 3v22h10"/><path d="M9 9h9M9 13h9M9 17h5"/><circle cx="21" cy="21" r="5"/><path d="M21 18v6M18 21h6"/></svg>ADD PTO</div>
    </aside>
    <header class="topbar">
      <div class="user-chip"><span class="avatar" role="img" aria-label="User profile photo"></span>Daniel Marsh <span class="caret">⌄</span></div>
      <nav class="tools">
        <div class="tool"><svg viewBox="0 0 16 16"><circle cx="8" cy="8" r="2.5"/><circle cx="8" cy="8" r="6"/></svg>SETTINGS</div>
        <div class="tool"><svg viewBox="0 0 16 16"><circle cx="8" cy="8" r="6.5"/><circle cx="8" cy="7" r="2.5"/><path d="M4 13c1-2 2.5-3 4-3s3 1 4 3"/></svg>PROFILE</div>
        <div class="tool"><svg viewBox="0 0 16 16"><path d="M4 12V7a4 4 0 0 1 8 0v5zM3 12h10M7 14h2"/></svg>NOTIFICATION</div>
        <div class="tool"><svg viewBox="0 0 16 16"><path d="M8 2v6M5 4a5.5 5.5 0 1 0 6 0"/></svg>LOGOUT</div>
      </nav>
    </header>
    <h1 class="today-title">TODAYS EVENT (1)</h1>
    <div class="today-person"><span class="avatar" role="img" aria-label="Photo of Daniel Marsh"><i class="online"></i></span><div>Daniel Marsh<br>Vocation</div></div>
    <div class="toolbar">
      <div class="btn-plain" style="left:0;width:69px">TODAY</div>
      <div class="btn-plain" style="left:77px;width:24px">‹</div>
      <div class="btn-plain" style="left:101px;width:24px">›</div>
      <div class="month-label">AUGUST 2020</div>
      <div class="view-switch"><span class="is-on">MONTH</span><span>WEEK</span><span>DAY</span></div>
    </div>
    <div class="calendar">
      <div class="cal-head"><span>SUNDAY</span><span>MONDAY</span><span>TUESDAY</span><span>WEDNESDAY</span><span>THURSDAY</span><span>FRIDAY</span><span>SATURDAY</span></div>
      <div class="cal-grid">
        <div class="day is-out"><span class="day-num">26</span></div><div class="day is-out"><span class="day-num">27</span></div><div class="day is-out"><span class="day-num">28</span></div><div class="day is-out"><span class="day-num">29</span></div><div class="day is-out"><span class="day-num">30</span></div><div class="day is-out"><span class="day-num">31</span></div><div class="day"><span class="day-num">01</span></div>
        <div class="day"><span class="day-num">02</span></div><div class="day"><span class="day-num">03</span></div><div class="day ev-cyan"><span class="day-num">04</span><span class="ev">12a Rowan Marsh<br>Vocation<br>4 a Clara Oakes<br>Vocations</span></div><div class="day"><span class="day-num">05</span></div><div class="day"><span class="day-num">06</span></div><div class="day"><span class="day-num">07</span></div><div class="day"><span class="day-num">08</span></div>
        <div class="day"><span class="day-num">09</span></div><div class="day"><span class="day-num">10</span></div><div class="day"><span class="day-num">11</span></div><div class="day"><span class="day-num">12</span></div><div class="day"><span class="day-num">13</span></div><div class="day"><span class="day-num">14</span></div><div class="day ev-green"><span class="day-num">15</span><span class="ev">12a Daniel Marsh<br>Vocation</span></div>
        <div class="day ev-blue"><span class="day-num">16</span><span class="ev">Daniel Marsh<br>Vocation</span></div><div class="day"><span class="day-num">17</span></div><div class="day"><span class="day-num">18</span></div><div class="day"><span class="day-num">19</span></div><div class="day"><span class="day-num">20</span></div><div class="day"><span class="day-num">21</span></div><div class="day"><span class="day-num">22</span></div>
        <div class="day"><span class="day-num">23</span></div><div class="day"><span class="day-num">24</span></div><div class="day"><span class="day-num">25</span></div><div class="day"><span class="day-num">26</span></div><div class="day"><span class="day-num">27</span></div><div class="day"><span class="day-num">28</span></div><div class="day"><span class="day-num">29</span></div>
        <div class="day"><span class="day-num">29</span></div><div class="day"><span class="day-num">30</span></div><div class="day"><span class="day-num">31</span></div><div class="day is-out"><span class="day-num">01</span></div><div class="day is-out"><span class="day-num">02</span></div><div class="day is-out"><span class="day-num">03</span></div><div class="day is-out"><span class="day-num">04</span></div>
      </div>
    </div>
    <p class="footer">© 2020 Restday. All Rights Reserved</p>
  </section>

  <!-- Add PTO modal screen -->
  <section class="screen screen--modal">
    <aside class="sidebar">
      <div class="brand">RESTDAY<span class="brand-dot"></span></div>
      <div class="nav-item"><svg viewBox="0 0 28 28"><circle cx="9" cy="9" r="4"/><circle cx="19" cy="9" r="4"/><circle cx="14" cy="18" r="4"/><path d="M6 26c1-3 4-4 8-4s7 1 8 4"/></svg>TEAMS</div>
      <div class="nav-item"><svg viewBox="0 0 28 28"><circle cx="14" cy="9" r="5"/><path d="M5 26c1-6 5-9 9-9s8 3 9 9"/><circle cx="20" cy="21" r="3"/></svg>MEMBERS</div>
      <div class="nav-item"><svg viewBox="0 0 28 28"><rect x="4" y="5" width="20" height="18"/><rect x="7" y="8" width="14" height="12"/><path d="M7 18l5-5 4 4 2-2 3 3"/></svg>PTO TYPES</div>
      <div class="nav-item is-active"><svg viewBox="0 0 28 28"><path d="M6 3h12l3 3v10M6 3v22h10"/><path d="M9 9h9M9 13h9M9 17h5"/><circle cx="21" cy="21" r="5"/><path d="M21 18v6M18 21h6"/></svg>ADD PTO</div>
    </aside>
    <header class="topbar">
      <div class="user-chip"><span class="avatar" role="img" aria-label="User profile photo"></span>Daniel Marsh <span class="caret">⌄</span></div>
      <nav class="tools">
        <div class="tool"><svg viewBox="0 0 16 16"><circle cx="8" cy="8" r="2.5"/><circle cx="8" cy="8" r="6"/></svg>SETTINGS</div>
        <div class="tool"><svg viewBox="0 0 16 16"><circle cx="8" cy="8" r="6.5"/><circle cx="8" cy="7" r="2.5"/><path d="M4 13c1-2 2.5-3 4-3s3 1 4 3"/></svg>PROFILE</div>
        <div class="tool"><svg viewBox="0 0 16 16"><path d="M4 12V7a4 4 0 0 1 8 0v5zM3 12h10M7 14h2"/></svg>NOTIFICATION</div>
        <div class="tool"><svg viewBox="0 0 16 16"><path d="M8 2v6M5 4a5.5 5.5 0 1 0 6 0"/></svg>LOGOUT</div>
      </nav>
    </header>
    <h1 class="today-title">TODAYS EVENT (1)</h1>
    <div class="today-person"><span class="avatar" role="img" aria-label="Photo of Daniel Marsh"><i class="online"></i></span><div>Daniel Marsh<br>Vocation</div></div>
    <div class="toolbar">
      <div class="btn-plain" style="left:0;width:69px">TODAY</div>
      <div class="btn-plain" style="left:77px;width:24px">‹</div>
      <div class="btn-plain" style="left:101px;width:24px">›</div>
      <div class="month-label">AUGUST 2020</div>
      <div class="view-switch"><span class="is-on">MONTH</span><span>WEEK</span><span>DAY</span></div>
    </div>
    <div class="calendar">
      <div class="cal-head"><span>SUNDAY</span><span>MONDAY</span><span>TUESDAY</span><span>WEDNESDAY</span><span>THURSDAY</span><span>FRIDAY</span><span>SATURDAY</span></div>
      <div class="cal-grid">
        <div class="day is-out"><span class="day-num">26</span></div><div class="day is-out"><span class="day-num">27</span></div><div class="day is-out"><span class="day-num">28</span></div><div class="day is-out"><span class="day-num">29</span></div><div class="day is-out"><span class="day-num">30</span></div><div class="day is-out"><span class="day-num">31</span></div><div class="day"><span class="day-num">01</span></div>
        <div class="day"><span class="day-num">02</span></div><div class="day"><span class="day-num">03</span></div><div class="day ev-cyan"><span class="day-num">04</span><span class="ev">12a Rowan Marsh<br>Vocation<br>4 a Clara Oakes<br>Vocations</span></div><div class="day"><span class="day-num">05</span></div><div class="day"><span class="day-num">06</span></div><div class="day"><span class="day-num">07</span></div><div class="day"><span class="day-num">08</span></div>
        <div class="day"><span class="day-num">09</span></div><div class="day"><span class="day-num">10</span></div><div class="day"><span class="day-num">11</span></div><div class="day"><span class="day-num">12</span></div><div class="day"><span class="day-num">13</span></div><div class="day"><span class="day-num">14</span></div><div class="day ev-green"><span class="day-num">15</span><span class="ev">12a Daniel Marsh<br>Vocation</span></div>
        <div class="day ev-blue"><span class="day-num">16</span><span class="ev">Daniel Marsh<br>Vocation</span></div><div class="day"><span class="day-num">17</span></div><div class="day"><span class="day-num">18</span></div><div class="day"><span class="day-num">19</span></div><div class="day"><span class="day-num">20</span></div><div class="day"><span class="day-num">21</span></div><div class="day"><span class="day-num">22</span></div>
        <div class="day"><span class="day-num">23</span></div><div class="day"><span class="day-num">24</span></div><div class="day"><span class="day-num">25</span></div><div class="day"><span class="day-num">26</span></div><div class="day"><span class="day-num">27</span></div><div class="day"><span class="day-num">28</span></div><div class="day"><span class="day-num">29</span></div>
        <div class="day"><span class="day-num">29</span></div><div class="day"><span class="day-num">30</span></div><div class="day"><span class="day-num">31</span></div><div class="day is-out"><span class="day-num">01</span></div><div class="day is-out"><span class="day-num">02</span></div><div class="day is-out"><span class="day-num">03</span></div><div class="day is-out"><span class="day-num">04</span></div>
      </div>
    </div>
    <p class="footer">© 2020 Restday. All Rights Reserved</p>
    <div class="shade"></div>
    <div class="modal">
      <div class="modal-head">ADD PTO<span class="modal-close">✖</span></div>
      <span class="field-label" style="top:70px">Member</span>
      <div class="field" style="top:93px">Daniel Marsh<span class="arrow">▼</span></div>
      <span class="field-label" style="top:142px">PTO Type</span>
      <div class="field" style="top:165px">Vocation<span class="arrow">▼</span></div>
      <span class="field-label" style="top:213px">Start Date</span>
      <div class="field" style="top:236px">08 / 11 / 2020<svg viewBox="0 0 12 12"><rect x="1" y="2" width="10" height="9"/><path d="M1 5h10M4 1v2M8 1v2"/></svg></div>
      <span class="field-label" style="top:285px">End Date</span>
      <div class="field" style="top:307px">08 / 14 / 2020<svg viewBox="0 0 12 12"><rect x="1" y="2" width="10" height="9"/><path d="M1 5h10M4 1v2M8 1v2"/></svg></div>
      <div class="modal-btn modal-btn--close">CLOSE</div>
      <div class="modal-btn modal-btn--save">SAVE</div>
    </div>
  </section>

  <!-- Admin teams screen -->
  <section class="screen screen--admin">
    <aside class="sidebar">
      <div class="brand">RESTDAY<span class="brand-dot"></span></div>
      <div class="nav-item is-active"><svg viewBox="0 0 28 28"><circle cx="9" cy="9" r="4"/><circle cx="19" cy="9" r="4"/><circle cx="14" cy="18" r="4"/><path d="M6 26c1-3 4-4 8-4s7 1 8 4"/></svg>TEAMS</div>
      <div class="nav-item"><svg viewBox="0 0 28 28"><circle cx="14" cy="9" r="5"/><path d="M5 26c1-6 5-9 9-9s8 3 9 9"/><circle cx="20" cy="21" r="3"/></svg>MEMBERS</div>
      <div class="nav-item"><svg viewBox="0 0 28 28"><rect x="4" y="5" width="20" height="18"/><rect x="7" y="8" width="14" height="12"/><path d="M7 18l5-5 4 4 2-2 3 3"/></svg>PTO TYPES</div>
      <div class="nav-item"><svg viewBox="0 0 28 28"><path d="M6 3h12l3 3v10M6 3v22h10"/><path d="M9 9h9M9 13h9M9 17h5"/><circle cx="21" cy="21" r="5"/><path d="M21 18v6M18 21h6"/></svg>ADD PTO</div>
    </aside>
    <header class="topbar">
      <div class="search"><span>Search</span><b><svg viewBox="0 0 12 12"><circle cx="5" cy="5" r="3.5"/><path d="M8 8l3 3"/></svg></b></div>
      <nav class="tools">
        <div class="tool"><svg viewBox="0 0 16 16"><circle cx="8" cy="8" r="2.5"/><circle cx="8" cy="8" r="6"/></svg>SETTINGS</div>
        <div class="tool"><svg viewBox="0 0 16 16"><circle cx="8" cy="8" r="6.5"/><circle cx="8" cy="7" r="2.5"/><path d="M4 13c1-2 2.5-3 4-3s3 1 4 3"/></svg>PROFILE</div>
        <div class="tool"><svg viewBox="0 0 16 16"><path d="M4 12V7a4 4 0 0 1 8 0v5zM3 12h10M7 14h2"/></svg>NOTIFICATION</div>
        <div class="tool"><svg viewBox="0 0 16 16"><path d="M8 2v6M5 4a5.5 5.5 0 1 0 6 0"/></svg>LOGOUT</div>
      </nav>
    </header>
    <div class="entries">SHOW<span class="select">20 <small>⌄</small></span>ENTRIES</div>
    <div class="table-card">
      <table class="data-table">
        <colgroup><col style="width:88px"><col style="width:89px"><col style="width:178px"><col style="width:88px"><col style="width:90px"><col style="width:89px"></colgroup>
        <thead><tr><th>TEAM NAME</th><th>SUPERVISOR</th><th>TEAM DESC</th><th>RESOURCE COUNT</th><th>STATUS</th><th>NEW</th></tr></thead>
        <tbody>
          <tr><td>Nursing</td><td>Clara Oakes</td><td>Lorem ipsum dolor sit amet, consec tetur adipiscing elitsed do eiusmod tempo incididunt ut labore et dolore</td><td>0</td><td>Active</td><td>Edit<span class="link">Delete</span></td></tr>
          <tr><td>Medical</td><td>Lionel Marsh</td><td>Lorem ipsum dolor sit amet, consec tetur adipiscing elitsed do eiusmod tempo incididunt ut labore et dolore</td><td>0</td><td>Active</td><td>Edit<span class="link">Delete</span></td></tr>
          <tr><td>Engineering</td><td>Clara Oakes</td><td>Lorem ipsum dolor sit amet, consec tetur adipiscing elitsed do eiusmod tempo incididunt ut labore et dolore</td><td>1</td><td>Active</td><td>Edit<span class="link">Delete</span></td></tr>
        </tbody>
      </table>
      <p class="showing">Showing 1 to 3 of Entries</p>
      <div class="pager"><span>1</span><span>2</span><span>3</span><span>Next ›</span></div>
    </div>
    <p class="footer">© 2020 Restday. All Rights Reserved</p>
  </section>

</div>
</body>
</html>
```